Children's Party Business needs a Business Card design!

We need a double sided, colour business card design.
The company name is "Maplewood Kids' Celebrations". We want one side to feature this logo.
We want the second side to feature the two branches "The Caped Crusade Adventure" and "The Fairytale Gala Adventure". I have attached logos for each of these below. When using these, I suggest removing the tagline & image from the logos, as those elements are already featured in the "Maplewood Kids' Celebration" logo.
To be included:
www.maplewoodkidscelebrations.com.au
1300 471 608
Optional text- "Making Dreams a Reality"
Optional photos- I've attached a bunch of our Character photos, which can be used if you please!
To give you an idea of the business, see The Caped Crusade Adventure website (under development):
http://qorvint.com/demo/capedcrusadeadventure/
Target Market(s)
Parents
Industry/Entity Type
Business
Contact Information for Business Card
To be included:
1300 471 608
Colors
Designer to choose colors to be used in the design.
Look and feel

```html
<!DOCTYPE html>
<html lang="en">
<head>
<meta charset="utf-8">
<title>Maplewood Kids' Celebrations – Business Card</title>
<link href="https://fonts.googleapis.com/css2?family=Fredoka:wght@600&family=Work+Sans:wght@400;500&display=swap" rel="stylesheet">
<style>
  :root {
    --backdrop: #3a302b;
    --navy: #1d2f66;
    --ink: #22305e;
    --sky: #5fb8e8;
    --white: #ffffff;
    --rule: #8fcdef;
    --soft-rule: #3d5190;
    --ghost-a: #eef1f5;
    --ghost-b: #f6e9ee;
    --brand-pink: #e9418c;
    --brand-gold: #f4c21b;
    --tagline: #b9c2e0;
  }
  * { box-sizing: border-box; margin: 0; padding: 0; }
  html, body { width: 1200px; height: 716px; overflow: hidden; }
  body {
    background: var(--backdrop);
    font-family: "Work Sans", Arial, sans-serif;
    position: relative;
  }
  .card {
    position: absolute;
    top: 208px;
    width: 525px;
    height: 300px;
    border-radius: 3px;
    box-shadow: 0 12px 30px rgba(0,0,0,.45);
    overflow: hidden;
  }
  .card--front { left: 45px; background: var(--navy); }
  .card--back { left: 630px; background: var(--white); }

  /* Front: the two branches */
  .branches {
    position: absolute;
    inset: 0;
    display: flex;
    flex-direction: column;
    align-items: center;
    justify-content: center;
    gap: 16px;
  }
  .branch {
    display: flex; align-items: center; gap: 12px;
    font-family: "Fredoka", "Work Sans", sans-serif;
    font-weight: 600;
    font-size: 27px;
    line-height: 1.1;
    color: var(--white);
    white-space: nowrap;
  }
  .branch__dot { width: 16px; height: 16px; border-radius: 50%; flex: none; }
  .branch__dot--fairytale { background: var(--brand-pink); }
  .branch__dot--caped { background: var(--brand-gold); }
  .branches__divider { width: 60px; height: 1px; background: var(--soft-rule); }
  .branches__tagline {
    margin-top: 4px;
    font-size: 11px;
    letter-spacing: .12em;
    text-transform: uppercase;
    color: var(--tagline);
  }

  /* Back: contact side */
  .back-brand {
    position: absolute; left: 34px; top: 34px;
    display: flex; align-items: center; gap: 10px;
    font-family: "Fredoka", "Work Sans", sans-serif;
    font-weight: 600;
    font-size: 22px;
    color: var(--ink);
  }
  .back-brand__dot { width: 14px; height: 14px; border-radius: 50%; background: var(--sky); }

  .contact-person { position: absolute; left: 34px; top: 110px; }
  .contact-person__name {
    font-size: 21px; letter-spacing: .06em; color: var(--sky);
    text-transform: uppercase; font-weight: 400;
  }
  .contact-person__role {
    font-size: 11px; letter-spacing: .06em; color: var(--ink);
    text-transform: uppercase; margin-top: 2px;
  }
  .contact-rule {
    position: absolute; left: 34px; right: 34px; top: 163px;
    height: 1px; background: var(--rule); z-index: 2;
  }
  .contact-list {
    position: absolute; left: 34px; top: 176px;
    list-style: none; font-size: 12.5px; line-height: 1.75; color: var(--ink);
    z-index: 2;
  }
  .contact-list b { font-weight: 400; color: var(--sky); margin-right: 4px; }

  .hero-ghost {
    position: absolute; right: 20px; top: 95px;
    width: 150px; height: 205px;
    border-radius: 70px 70px 0 0;
    background: linear-gradient(180deg, var(--ghost-b), var(--ghost-a));
    opacity: .85;
  }
</style>
</head>
<body>
  <section class="card card--front">
    <div class="branches">
      <div class="branch"><span class="branch__dot branch__dot--fairytale"></span>The Fairytale Gala Adventure</div>
      <div class="branches__divider"></div>
      <div class="branch"><span class="branch__dot branch__dot--caped"></span>The Caped Crusade Adventure</div>
      <div class="branches__tagline">Maplewood Kids' Celebrations</div>
    </div>
  </section>

  <section class="card card--back">
    <div class="back-brand"><span class="back-brand__dot"></span>Maplewood Kids' Celebrations</div>
    <div class="hero-ghost" role="img" aria-label="Faint silhouette of a superhero holding party balloons"></div>
    <div class="contact-person">
      <h1 class="contact-person__name">Dana Whitlock</h1>
      <p class="contact-person__role">Director</p>
    </div>
    <div class="contact-rule"></div>
    <ul class="contact-list">
      <li><b>P :</b>1300 471 608 &nbsp;<b>E :</b>info@maplewoodkidscelebrations.com.au</li>
      <li><b>W :</b>www.maplewoodkidscelebrations.com.au</li>
      <li><b>A :</b>2871C Birch Lane, Alder Valley, AB, T9X 4R2</li>
    </ul>
  </section>
</body>
</html>
```